Book Cover Contest: "Roads Toward Quiet Grace"

The KR Verlag Islamic Library invites designers and artists to design a cover for the upcoming book “Roads Toward Quiet Grace”.

This inspiring work is by Shaikh Yūsuf al-Karīm ibn Hāmid ibn Ubaydillah al-Mazrūʿī (d. 1376 AH/1957 CE), a renowned Islamic scholar. In his writing, he imparts timeless principles for inner peace and true happiness based on Islamic faith and spiritual knowledge.

Important details for the cover design:
The cover should reflect the theme of the book: paths to happiness, spiritual satisfaction, a fulfilled life.
It may contain both modern and traditional elements, but should be clear, appealing and reader-friendly.
The title “Roads toward quiet grace” should be clearly visible.
Author: Šaiḫ Yūsuf al-Karīm ibn Ḥāmid ibn ʿUbaydillah al-Mazrūʿī
Translation: Marlene Kürten

KR Verlag Islamic Library

Do you have a creative idea for the cover? Then join in and design the face of this inspiring work!

Target Market(s)

Islamic

Font styles to use
Decorative
Script

Requirements
Should not have
• No mosque silhouette, no hanging lamp,

```html
<!DOCTYPE html>
<html lang="de">
<head>
<meta charset="utf-8">
<title>Wege zu einer stillen Anmut</title>
<link rel="stylesheet" href="https://fonts.googleapis.com/css2?family=Great+Vibes&family=Arimo:wght@700&display=swap">
<style>
  :root {
    --night: #020308;
    --deep: #050b16;
    --glow: #a9d6ec;
    --glow-mid: #2f6f96;
    --glow-edge: #0b2236;
    --haze: #6f8594;
    --floor: #4a2535;
    --floor-dark: #0c070b;
    --ink: #ffffff;
    --shadow: rgba(0, 0, 0, 0.85);
  }
  * { margin: 0; padding: 0; box-sizing: border-box; }
  html, body {
    width: 776px;
    height: 1200px;
    overflow: hidden;
    background: var(--night);
  }
  .cover {
    position: relative;
    width: 776px;
    height: 1200px;
    overflow: hidden;
    background:
      radial-gradient(ellipse 340px 330px at 388px 840px, var(--glow) 0%, var(--glow-mid) 30%, var(--glow-edge) 62%, transparent 100%),
      linear-gradient(180deg, var(--night) 0%, var(--deep) 60%, var(--night) 100%);
    color: var(--ink);
  }
  .scene {
    position: absolute;
    left: 0;
    top: 780px;
    width: 776px;
    height: 420px;
  }
  .title {
    position: absolute;
    left: 0;
    top: 40px;
    width: 100%;
    text-align: center;
    font-family: "Great Vibes", cursive;
    font-weight: 400;
    font-size: 132px;
    line-height: 145px;
    text-shadow: 3px 4px 3px var(--shadow);
  }
  .author {
    position: absolute;
    left: 0;
    top: 660px;
    width: 100%;
    text-align: center;
    font-family: "Arimo", sans-serif;
    font-weight: 700;
  }
  .author-name {
    font-size: 28px;
    line-height: 36px;
  }
  .author-dates {
    font-size: 19px;
    line-height: 24px;
  }
  .credits {
    position: absolute;
    left: 0;
    top: 1014px;
    width: 100%;
    text-align: center;
    font-family: "Great Vibes", cursive;
    font-size: 35px;
    line-height: 38px;
    text-shadow: 2px 2px 2px var(--shadow);
  }
  .publisher {
    position: absolute;
    left: 0;
    top: 1122px;
    width: 100%;
    text-align: center;
    font-family: "Arimo", sans-serif;
    font-weight: 700;
    font-size: 20px;
  }
</style>
</head>
<body>
  <main class="cover">
    <svg class="scene" viewBox="0 0 776 420" preserveAspectRatio="none" role="img" aria-label="Aufgeschlagenes Buch auf einem hölzernen Lesepult neben einer kleinen Laterne auf einem Teppich, von hinten hell angestrahlt">
      <defs>
        <linearGradient id="scene-fade" x1="0" y1="0" x2="0" y2="1">
          <stop offset="0" stop-color="#1a3a52" stop-opacity="0"/>
          <stop offset="0.3" stop-color="var(--haze)" stop-opacity="0.5"/>
          <stop offset="0.5" stop-color="var(--floor)" stop-opacity="0.9"/>
          <stop offset="0.62" stop-color="var(--floor-dark)"/>
          <stop offset="1" stop-color="var(--night)"/>
        </linearGradient>
      </defs>
      <rect x="0" y="0" width="776" height="420" fill="url(#scene-fade)"/>
    </svg>

    <h1 class="title">Wege<br>zu einer<br>stillen<br>Anmut</h1>

    <div class="author">
      <p class="author-name">Šaiḫ Yūsuf al-Karīm ibn<br>Ḥāmid ibn ʿUbaydillah al-Mazrūʿī</p>
      <p class="author-dates">(gest. 1376 n. H./1957 n. Chr.)</p>
    </div>

    <div class="credits">
      <p class="translator">Übersetzung: Marlene Kürten</p>
      <p class="editor">Lektorat: Dr. Tobias Idris Brand</p>
    </div>

    <p class="publisher">KR Verlag Islamic Library</p>
  </main>
</body>
</html>
```